I make small projects usually ranging from cutting boards, kitchen utensils , cedar gardens projects, basically anything I can fit in a 2 car garage workshop. I've been ask by numerous people if I have website or a facebook page or something where they go look at my products/abilities. I pretty much make anything anyone wants out of wood and can customize to their needs.

R.T.Belcourt Custom Woodworks Inc. is my business name.

At this time I'm currently seeking a branding logo and business card set for my new business. I'm based out of the city of Edmonton, Alberta, Canada. My target market would be Middle class to upper class, new home-owners who like quality products to compliment the look of their new homes and property at decent prices. Although this my current work practice I am thinking I venture into finish carpentry long term and that is why I choose the name to be more formal. However I would the design to different that just a plain card. Would like to incorporate wood grain color or pattern. I would like a slogan or logo text, but I have no idea what ill leave that up to you and see what you come back with.

Target Market(s)

My target market would be Middle class to upper class, new home-owners who like quality products to compliment the look of their new homes and property at decent prices.

Industry/Entity Type

Carpentry

Contact Information for Business Card

Rowan T. Belcourt
Craftsmen

R.T.Belcourt Custom Woodworks Inc
Address: 2817 Thornbury Way SW, Edmonton, A.B., T5K 2P8
Cell: (780) 555-0193
Smtp: rtbwoodworks@examplemail.net
Website: XXXXXXX yet to be determined
Facebook: R.T.Belcourt Custom Woodworks Inc.

Logo styles of interest
Emblem Logo
Pictorial/Combination Logo
Abstract Logo
Lettermark Logo
Requirements
Nice to have
• Although there is a allot information in the business card detail area, feel free to alter as you see fir. example: remove business address, website(as i dont have one yet)

```html
<!DOCTYPE html>
<html lang="en">
<head>
<meta charset="utf-8">
<title>R.T.Belcourt Custom Woodworks Inc. – Business Card</title>
<link rel="stylesheet" href="https://fonts.googleapis.com/css2?family=Montserrat:wght@400;500;600;800&display=swap">
<style>
  :root {
    --navy: #0d3a5c;
    --white: #ffffff;
    --paper: #f7f8f9;
    --wood-light: #c89a64;
    --wood-mid: #a8743f;
    --wood-dark: #7d5128;
    --ink: #4a5560;
    --stage: #e4e5e6;
  }
  * { box-sizing: border-box; margin: 0; padding: 0; }
  html, body {
    width: 1200px; height: 730px; overflow: hidden;
    background: var(--stage);
    font-family: "Montserrat", Arial, sans-serif;
  }
  .canvas {
    position: relative; width: 1200px; height: 730px;
    display: flex; align-items: center; justify-content: center; gap: 60px;
  }
  .card {
    position: relative; width: 520px; height: 297px; overflow: hidden;
    box-shadow: 0 6px 18px rgba(0,0,0,0.12);
  }
  /* Front */
  .card-front { background: var(--navy); color: var(--white); }
  .card-front .brand {
    position: absolute; left: 0; right: 0; top: 100px; text-align: center;
  }
  .brand-name {
    font-weight: 800; font-size: 64px; letter-spacing: 1px; line-height: 1;
    color: var(--white);
  }
  .brand-tagline {
    margin-top: 10px; font-size: 11px; font-weight: 500; letter-spacing: 3px;
    text-transform: uppercase; color: var(--white);
  }
  /* Back */
  .card-back { background: var(--paper); color: var(--ink); }
  .card-back .brand-name {
    position: absolute; right: 110px; top: 62px;
    font-size: 34px; color: var(--navy);
  }
  .contact {
    position: absolute; left: 42px; top: 112px; font-size: 11px; line-height: 1.6;
  }
  .contact .person { font-size: 13px; font-weight: 600; color: var(--navy); }
  .contact .role { font-size: 11px; margin-bottom: 12px; }
  .contact dl { display: grid; grid-template-columns: 22px auto; }
  .contact dt, .contact dd { font-weight: 400; }
  .card-back .wood-block {
    position: absolute; right: 0; bottom: 22px; width: 100px; height: 48px;
    background: linear-gradient(100deg, var(--wood-dark) 0%, var(--wood-light) 35%, var(--wood-mid) 60%, var(--wood-light) 82%, var(--wood-dark) 100%);
  }
  .card-back svg.band { position: absolute; left: 0; bottom: 0; }
</style>
</head>
<body>
<main class="canvas">
  <section class="card card-front" aria-label="Business card front">
    <div class="brand">
      <div class="brand-name">Belcourt</div>
      <div class="brand-tagline">Custom Woodworks Inc</div>
    </div>
  </section>

  <section class="card card-back" aria-label="Business card back">
    <div class="brand-name">Belcourt</div>
    <div class="contact">
      <p class="person">Rowan T. Belcourt</p>
      <p class="role">Craftsmen</p>
      <dl>
        <dt>C :</dt><dd>(780) 555-0193</dd>
        <dt>E :</dt><dd>rtbwoodworks@examplemail.net</dd>
        <dt>A :</dt><dd>2817 Thornbury Way SW, Edmonton, A.B., T5K 2P8</dd>
      </dl>
    </div>
    <div class="wood-block" role="img" aria-label="Wood grain texture in warm timber tones"></div>
    <svg class="band" width="520" height="22" viewBox="0 0 520 22" aria-hidden="true">
      <polygon points="150,0 520,0 520,22 130,22" fill="var(--navy)"/>
    </svg>
  </section>
</main>
</body>
</html>
```